" A venda é feita porta á porta. Os produtos são divulgados nas redes sociais. O cliente faz contato e solicita uma visita. Um novo projeto esta sendo desenvolvido para montar uma loja móvel em uma van furgão. "

```html
<!DOCTYPE html>
<html lang="pt-BR">
<head>
<meta charset="utf-8">
<title>Serena – Tag</title>
<link href="https://fonts.googleapis.com/css2?family=Montserrat:wght@500;600&display=swap" rel="stylesheet">
<style>
  :root {
    --bg-light: #f4f4f4;
    --bg-dark: #cfcfcf;
    --rose-1: #e6c2b3;
    --rose-2: #c98f80;
    --rose-3: #f3d9cd;
    --mauve: #8c7070;
    --mauve-text: #8a6c6c;
    --name-light: #ecc9bb;
    --white: #ffffff;
    --ink-light: #f6ecea;
    --ink-dark: #6f5858;
  }
  * { margin: 0; padding: 0; box-sizing: border-box; }
  html, body { width: 1200px; height: 1200px; overflow: hidden; }
  body {
    background: radial-gradient(ellipse at 50% 45%, var(--bg-light) 40%, var(--bg-dark) 100%);
    font-family: "Montserrat", sans-serif;
    position: relative;
  }
  .header-band {
    position: absolute; left: 396px; top: 0; width: 408px; height: 67px;
    background: linear-gradient(90deg, var(--rose-2), var(--rose-3) 50%, var(--rose-2));
    border-radius: 0 0 10px 10px;
    display: flex; align-items: center; justify-content: center;
    color: var(--white); font-weight: 600; font-size: 26px; letter-spacing: 8px;
  }
  .tag {
    position: absolute; top: 168px; width: 375px; height: 960px;
    border-radius: 8px 40px 8px 40px;
    overflow: hidden;
    box-shadow: 0 14px 30px rgba(0,0,0,0.22);
  }
  .tag--dark { left: 187px; background: var(--mauve); }
  .tag--light { left: 653px; background: var(--white); }
  .tag__hole {
    position: absolute; left: 166px; top: 14px; width: 44px; height: 44px;
    border-radius: 50%; background: var(--bg-light);
    box-shadow: inset 0 2px 4px rgba(0,0,0,0.25);
  }
  .brand {
    position: absolute; left: 0; right: 0; top: 410px; text-align: center;
  }
  .brand__name {
    font-weight: 600; font-size: 58px; letter-spacing: 6px; line-height: 1;
  }
  .brand__tagline {
    margin-top: 22px; font-weight: 500; font-size: 18px; letter-spacing: 3px;
    color: var(--rose-2);
  }
  .tag--dark .brand__name { color: var(--name-light); }
  .tag--dark .brand__tagline { color: var(--rose-1); }
  .tag--light .brand__name { color: var(--mauve-text); }
  .contacts {
    position: absolute; left: 17px; top: 716px; list-style: none;
  }
  .contacts__item {
    display: flex; align-items: center; height: 43px;
    font-size: 23px; font-weight: 500;
  }
  .tag--dark .contacts__item { color: var(--ink-light); }
  .tag--light .contacts__item { color: var(--ink-dark); }
  .contacts__icon {
    width: 26px; height: 26px; margin-right: 14px; border-radius: 4px;
    background: linear-gradient(135deg, var(--rose-1), var(--rose-2));
    display: flex; align-items: center; justify-content: center; flex: none;
  }
  .tag__band {
    position: absolute; left: 0; right: 0; bottom: 0; height: 100px;
    background: linear-gradient(90deg, var(--rose-2), var(--rose-3) 50%, var(--rose-2));
  }
</style>
</head>
<body>
  <div class="header-band">TAG</div>

  <div class="tag tag--dark">
    <div class="tag__hole"></div>
    <div class="brand">
      <div class="brand__name">Serena</div>
      <div class="brand__tagline">MODA E DEVOÇÃO</div>
    </div>
    <ul class="contacts">
      <li class="contacts__item">
        <span class="contacts__icon">
          <svg width="16" height="16" viewBox="0 0 24 24"><path fill="#fff" d="M6.6 10.8a15.1 15.1 0 0 0 6.6 6.6l2.2-2.2c.3-.3.7-.4 1-.2 1.1.4 2.3.6 3.6.6.6 0 1 .4 1 1V20c0 .6-.4 1-1 1A17 17 0 0 1 3 4c0-.6.4-1 1-1h3.5c.6 0 1 .4 1 1 0 1.3.2 2.5.6 3.6.1.3 0 .7-.2 1z"/></svg>
        </span>(27) 98765-4321
      </li>
      <li class="contacts__item"><span class="contacts__icon"></span>@serena.lojacatolica</li>
      <li class="contacts__item"><span class="contacts__icon"></span>/serena.lojacatolica</li>
    </ul>
    <div class="tag__band"></div>
  </div>

  <div class="tag tag--light">
    <div class="tag__hole"></div>
    <div class="brand">
      <div class="brand__name">Serena</div>
      <div class="brand__tagline">MODA E DEVOÇÃO</div>
    </div>
    <ul class="contacts">
      <li class="contacts__item">
        <span class="contacts__icon">
          <svg width="16" height="16" viewBox="0 0 24 24"><path fill="#fff" d="M6.6 10.8a15.1 15.1 0 0 0 6.6 6.6l2.2-2.2c.3-.3.7-.4 1-.2 1.1.4 2.3.6 3.6.6.6 0 1 .4 1 1V20c0 .6-.4 1-1 1A17 17 0 0 1 3 4c0-.6.4-1 1-1h3.5c.6 0 1 .4 1 1 0 1.3.2 2.5.6 3.6.1.3 0 .7-.2 1z"/></svg>
        </span>(27) 98765-4321
      </li>
      <li class="contacts__item"><span class="contacts__icon"></span>@serena.lojacatolica</li>
      <li class="contacts__item"><span class="contacts__icon"></span>/serena.lojacatolica</li>
    </ul>
    <div class="tag__band"></div>
  </div>
</body>
</html>
```